KPT Building And Maintenance

Need a very professional looking double sided Buisiness card with all my details phone number, name, email, license number.

Target Market(s)

construction industry

Industry/Entity Type

building

Contact Information for Business Card

Name Dale Whitcombe. Email Address Info@KPTBuilding.example.au mobile number 0452918730 licence number 871406D. web site

```html
<!DOCTYPE html>
<html lang="en">
<head>
<meta charset="utf-8">
<title>KPT Building And Maintenance – Business Card</title>
<link href="https://fonts.googleapis.com/css2?family=Exo+2:wght@400;600;700;800&display=swap" rel="stylesheet">
<style>
  :root {
    --page-bg: #ededee;
    --band-grey: #4a4a4b;
    --card-white: #ffffff;
    --card-black: #060809;
    --brand-blue: #3d95d5;
    --text-dark: #3a3a3a;
    --white: #ffffff;
  }
  * { box-sizing: border-box; margin: 0; padding: 0; }
  html, body {
    width: 1076px; height: 1200px; overflow: hidden;
    background: var(--page-bg);
    font-family: "Exo 2", sans-serif;
  }
  .canvas { position: relative; width: 1076px; height: 1200px; }

  .card {
    position: absolute;
    top: 368px;
    width: 322px;
    height: 184px;
    overflow: hidden;
  }
  .card--front { left: 278px; background: var(--card-white); }
  .card--back  { left: 634px; background: var(--card-black); }

  .front-band {
    height: 74px;
    background: var(--band-grey);
    display: flex;
    align-items: center;
    justify-content: center;
  }
  .wordmark {
    font-family: "Exo 2", sans-serif;
    font-weight: 800;
    color: var(--white);
    text-transform: uppercase;
    letter-spacing: 1px;
    line-height: 1;
    white-space: nowrap;
  }
  .front-band .wordmark { font-size: 34px; }

  .holder-name {
    position: absolute;
    right: 14px;
    top: 107px;
    font-size: 15px;
    font-weight: 600;
    color: var(--brand-blue);
  }
  .contact-list {
    position: absolute;
    right: 14px;
    top: 136px;
    list-style: none;
    text-align: right;
  }
  .contact-list li {
    display: flex;
    justify-content: flex-end;
    align-items: center;
    gap: 4px;
    font-size: 9.5px;
    line-height: 12.4px;
    color: var(--text-dark);
    white-space: nowrap;
  }
  .contact-list svg { width: 9px; height: 9px; flex: none; }

  .licence {
    position: absolute;
    left: 12px;
    top: 160px;
    font-size: 9.5px;
    line-height: 12.4px;
    color: var(--text-dark);
    white-space: nowrap;
  }
  .licence-number { color: var(--brand-blue); }

  .card--back {
    display: flex;
    align-items: center;
    justify-content: center;
  }
  .card--back .wordmark {
    font-size: 32px;
    text-align: center;
    line-height: 1.05;
  }
</style>
</head>
<body>
<main class="canvas">
  <section class="card card--front" aria-label="Business card front">
    <header class="front-band">
      <span class="wordmark">KPT Building</span>
    </header>
    <p class="holder-name">Dale Whitcombe</p>
    <ul class="contact-list">
      <li>045 291 8730
        <svg viewBox="0 0 10 10" aria-hidden="true"><circle cx="5" cy="5" r="4.6" fill="none" stroke="#3d95d5" stroke-width="0.9"/><path d="M3.2 2.6l1 1-.6.7c.4.8 1 1.4 1.8 1.8l.7-.6 1 1-.8.8C4.8 7.2 2.8 5.2 2.4 3.4z" fill="#3d95d5"/></svg>
      </li>
      <li>Info@KPTBuilding.example.au
        <svg viewBox="0 0 10 10" aria-hidden="true"><rect x="0.5" y="2" width="9" height="6" fill="#3d95d5"/><path d="M0.8 2.3L5 5.6l4.2-3.3" fill="none" stroke="#fff" stroke-width="0.8"/></svg>
      </li>
      <li>www.KPTBuilding.example.au
        <svg viewBox="0 0 10 10" aria-hidden="true"><circle cx="5" cy="5" r="4.5" fill="#3d95d5"/><path d="M0.5 5h9M5 0.5c-2.4 2.6-2.4 6.4 0 9M5 0.5c2.4 2.6 2.4 6.4 0 9" fill="none" stroke="#fff" stroke-width="0.6"/></svg>
      </li>
    </ul>
    <p class="licence">licence number <span class="licence-number">871406D</span></p>
  </section>

  <section class="card card--back" aria-label="Business card back">
    <span class="wordmark">KPT<br>Building</span>
  </section>
</main>
</body>
</html>
```